Zestra Design Prize - $10,000 tablet app design contest, Magazine Category

Zestra is a marketplace for uSlate App Templates (similar to PageLoom templates). We want you to design an app template for sale in our marketplace which targets B2B or B2C Magazine Apps (uSlate Apps created for examples such as Alumni magazine, employee magazine, sports magazine, fashion magazine etc).

It’s up to you to create pages or features for the App Template that you think are appropriate. Creativity will be rewarded! Here are some example pages or features that you could create:

• Contents
• Editor’s letter
• Event calendar
• News page
• Feature article
• Business articles
• Social media integration
• Animations and video

Your design should be Vibrant, Engaging and Contemporary. If you have an uSlate, download Zestra Viewer and download template examples in the download tab.

Your entry must include:
• A brief description of your template
• Preview images of all pages of your template

Attached to this project are free templates to help you get started with your design. We have included:
1. A free portfolio template for designers/photographers
2. Icons and artwork to use in your template
3. Blank pages template
4. Form template
5. Video ad template

If you are selected as a finalist you will be required to submit an .oproject file containing:
• Your LayoutCraft source files
• Preview images of your template
• All creative / stock assets used in the template (animations, video etc.)
• A text file with instructions on how to update the template
• A metadata .txt file containing template details and your information

How to enter:
1. Register at Marketplace and view the instructions under the welcome message https://marketplace.zestrahub.test/welcome
2. Download Zestra Editor: https://support.zestrahub.test/entries/58104926-zestra-editor
3. Use the free templates provided in this brief to create your designs and submit to ArtFlock
Updates

Reason: Due to the Christmas break we are extending the deadline of our competition. Thank you for time and effort - I will be providing feedback over the next couple of days! Best wishes, Melody

Hi All,

I have received many screenshots with some great designs! I just wanted to clarify that you are designing Zestra app templates including Zestra features and not just page designs?

Read Tips for First Time Zestrans to guide you through the template creation process

Before you start designing templates for Zestra Marketplace

·       Read the Quality Standards

·       Read the Copyright Information 

·       Use the Template Quality Checklist to ensure your template follows our guidelines. 

What should my project file contain?

·       A folder containing your source files, e.g. LayoutCraft. This must be named Source.

·       The Zestra content files. This must be named Bundle.

·       Instructions, explaining to a customer how to use your template.

Best wishes,

Melody

Reason: We are extending the competition by 7 days to give you more time!

Reason: We have received 3 complete designs for this contest so we are extending the deadline for 7 days Best wishes, Melody

Target Market(s)

Entrepreneurs who wish to create uSlate Apps by using our App design templates.

Industry/Entity Type

Fashion

Requirements
Must have
• You will need Zestra Editor to open the .oproject files attached to this brief. Get it here: https://support.zestrahub.test/entries/58104926-zestra-editor
Should not have
• • Low quality, fuzzy or blurry images
• Any stock images or content which you do not own the rights to
• Any material which could be considered inappropriate or offensive

```html
<!DOCTYPE html>
<html lang="en">
<head>
<meta charset="utf-8">
<title>Magazine Template – News and Event Calendar</title>
<link rel="stylesheet" href="https://fonts.googleapis.com/css2?family=Poppins:wght@500;600;700&family=Questrial&family=Arimo:wght@400;700&display=swap">
<style>
:root{
  --stage:#1b1b1b;
  --blue:#6699ff;
  --white:#ffffff;
  --yellow:#ffe22e;
  --ink:#111111;
  --photo-dark:#3f4a44;
  --photo-light:#b9c0bb;
  --sky:#3fb8ea;
  --sheet:#f2f3f5;
  --sheet-line:#c9ccd2;
  --ios-blue:#3d78d8;
  --key:#fdfdfd;
  --key-dark:#b5b9c2;
  --kbd:#d2d5db;
}
*{box-sizing:border-box;margin:0;padding:0}
html,body{width:918px;height:1200px;overflow:hidden;background:var(--stage)}
.canvas{position:relative;width:918px;height:1200px}
.screen{position:absolute;width:423px;height:564px;overflow:hidden}
.screen--news-a{left:18px;top:18px;background:var(--blue)}
.screen--news-b{left:477px;top:18px;background:var(--blue)}
.screen--calendar{left:18px;top:618px;height:565px}
.screen--add-event{left:477px;top:618px;height:565px}
.abs{position:absolute}

/* news */
.stripe-bar{position:absolute;left:10px;width:404px;height:20px;
  background:repeating-linear-gradient(90deg,var(--white) 0 4px,transparent 4px 11px)}
.headline-list{position:absolute;left:10px;list-style:none}
.headline{position:absolute;left:0;width:120px;font:700 14px/13px "Poppins",sans-serif;color:var(--white);letter-spacing:-.2px;white-space:nowrap}
.play{position:absolute;width:30px;height:30px}
.body-copy{position:absolute;left:156px;width:220px;font:10px/14px "Questrial",sans-serif;color:var(--white)}
.body-copy p{margin-bottom:14px}
.hint{position:absolute;left:156px;font:700 5.5px "Poppins",sans-serif;color:var(--white)}
.photo{position:absolute;left:156px;width:219px}
.photo--sky{top:300px;height:195px;background:linear-gradient(160deg,var(--sky) 0%,#8fd3f1 55%,#e9f4f8 100%)}
.photo--wall{top:535px;height:40px;background:linear-gradient(180deg,#e8ece8,#b7bdb8)}
.news-title{position:absolute;left:146px;top:95px;font:700 13px/13px "Poppins",sans-serif;color:var(--white);text-transform:uppercase}

.nav-btn{position:absolute;width:56px;height:56px;display:flex;flex-direction:column;align-items:center;justify-content:center;text-align:center;font:600 8px/9px "Poppins",sans-serif;color:var(--blue)}
.nav-btn small{font:500 6px "Poppins",sans-serif;opacity:.8;margin-bottom:4px}
.nav-btn--contents{border-radius:50%;background:var(--white)}
.nav-btn--cover{background:var(--yellow)}
.nav-btn--contents.on-photo{background:var(--blue);color:var(--white)}

/* calendar */
.calendar-photo{position:absolute;inset:0;background:linear-gradient(180deg,#4a5a58 0%,#7d8780 35%,var(--photo-light) 60%,#6e7a62 100%)}
.cal-title{position:absolute;left:0;font:600 96px/1 "Poppins",sans-serif;color:var(--yellow);letter-spacing:-5px;white-space:nowrap}
.cal-title--event{top:-14px}
.cal-title--calendar{top:44px;left:1px}
.cal-hint{position:absolute;top:122px;left:0;width:423px;text-align:center;font:600 7.5px "Poppins",sans-serif;color:var(--white);text-transform:uppercase}
.month{position:absolute;top:134px;height:420px;background:var(--yellow);overflow:hidden}
.month-name{position:absolute;top:0;left:2px;font:700 20px/22px "Poppins",sans-serif;color:var(--ink);letter-spacing:-.5px;white-space:nowrap}
.month-stripes{position:absolute;top:25px;left:0;right:0;height:10px;background:repeating-linear-gradient(90deg,var(--ink) 0 2px,transparent 2px 5px)}
.swipe-tag{position:absolute;top:158px;left:321px;width:26px;height:11px;background:var(--ink);color:var(--white);font:700 6px/11px "Poppins",sans-serif;text-align:center}
.event-date{position:absolute;font:700 13px "Poppins",sans-serif;color:var(--white)}
.event-text{position:absolute;font:500 11px/13px "Poppins",sans-serif;color:var(--ink)}
.dim{position:absolute;inset:0;background:rgba(0,0,0,.42)}

/* add event sheet */
.sheet{position:absolute;left:64px;top:112px;width:295px;height:320px;background:var(--sheet);border-radius:5px;overflow:hidden;font-family:"Arimo",sans-serif}
.sheet-bar{height:24px;background:linear-gradient(#e9ebef,#c9cdd4);display:flex;align-items:center;justify-content:space-between;padding:0 6px;font-size:11px;color:#555}
.sheet-btn{font-size:7px;padding:3px 5px;border-radius:3px;background:#8e939b;color:#fff}
.sheet-btn--done{background:var(--ios-blue)}
.field-group{margin:6px 16px 0;background:#fff;border:1px solid var(--sheet-line);border-radius:5px;font-size:8.5px;color:#333}
.field{padding:7px 8px;border-top:1px solid var(--sheet-line);display:flex;justify-content:space-between}
.field:first-child{border-top:0}
.field b{font-weight:700;color:#222}
.field .val{color:#3c5a8a}
.field .ph{color:#aaa}
.keyboard{position:absolute;left:0;top:418px;width:423px;height:147px;background:linear-gradient(#b9bdc6,#8f949e);padding:8px 6px 0;font-family:"Arimo",sans-serif}
.key-row{display:flex;gap:5px;margin-bottom:6px;justify-content:center}
.key{width:33px;height:31px;border-radius:5px;background:var(--key);display:flex;align-items:center;justify-content:center;font-size:13px;color:#222;box-shadow:0 1px 0 #666}
.key--dark{background:var(--key-dark);font-size:9px}
</style>
</head>
<body>
<main class="canvas">

  <!-- News page, layout A -->
  <section class="screen screen--news-a">
    <div class="stripe-bar" style="top:37px"></div>
    <ul class="headline-list">
      <li class="headline" style="top:87px">First Piece of<br>News.</li>
      <li class="headline" style="top:137px">Second<br>Piece of<br>News.</li>
      <li class="headline" style="top:201px">Third Piece of<br>News.</li>
      <li class="headline" style="top:251px">Fourth Piece<br>of News.</li>
    </ul>
    <svg class="play" style="left:114px;top:139px" viewBox="0 0 30 30"><circle cx="15" cy="15" r="15" fill="#fff"/><path d="M11 8 L22 15 L11 22Z" fill="var(--blue)"/></svg>
    <div class="body-copy" style="top:86px">
      <p>Morbi laoreet consequat nibh, sed posuere orci venenatis vel. Nam eu mi nunc. Aliquam erat volutpat. Vivamus in est eget lacus semper mattis eget nec dui. Cras eget pulvinar augue. Praesent eget tortor eu nulla porttitor aliquam. Sed auctor elementum quam vitae rhoncus.</p>
      <p>Elementum sit amet dictum sit amet, imperdiet vel tortor. Fusce viverra sapien eu velit tempus vestibulum. Proin eleifend leo ac risus cursus lacinia. Pellentesque id lorem eu sem fermentum tincidunt. Morbi placerat massa eu tellus placerat dapibus.</p>
    </div>
    <span class="hint" style="top:292px">Swipe images to view.</span>
    <div class="photo photo--sky" role="img" aria-label="Photo of a white tower against a blue sky with clouds"></div>
    <a class="nav-btn nav-btn--contents" style="left:10px;top:500px"><small>return</small>contents<br>page</a>
    <a class="nav-btn nav-btn--cover" style="left:79px;top:501px"><small>return</small>cover<br>page</a>
  </section>

  <!-- News page, layout B -->
  <section class="screen screen--news-b">
    <h1 class="news-title">In the news<br>recently...</h1>
    <div class="stripe-bar" style="top:172px"></div>
    <ul class="headline-list">
      <li class="headline" style="top:224px">First Piece of<br>News.</li>
      <li class="headline" style="top:274px">Second<br>Piece of<br>News.</li>
      <li class="headline" style="top:338px">Third Piece of<br>News.</li>
      <li class="headline" style="top:388px">Fourth Piece<br>of News.</li>
    </ul>
    <svg class="play" style="left:114px;top:225px" viewBox="0 0 30 30"><circle cx="15" cy="15" r="15" fill="#fff"/><path d="M11 8 L22 15 L11 22Z" fill="var(--blue)"/></svg>
    <div class="body-copy" style="top:222px">
      <p>Suspendisse elementum arcu sed dolor tincidunt venenatis. Aliquam erat volutpat. Proin molestie neque nec quam tempus condimentum. Morbi pretium ligula a elit blandit vulputate. Nullam lacinia urna et felis sollicitudin et pulvinar nisi vestibulum.</p>
      <p>Morbi laoreet consequat nibh, sed posuere orci venenatis vel. Nam eu mi nunc. Aliquam erat volutpat. Vivamus in est eget lacus semper mattis eget nec dui.</p>
      <p>Nunc magna erat, elementum sit amet dictum sit amet, imperdiet vel tortor. Fusce viverra sapien eu velit tempus vestibulum. Proin eleifend leo ac risus cursus lacinia. Pellentesque id lorem eu sem fermentum tincidunt. Morbi placerat massa eu tellus placerat dapibus. Cras eget pulvinar augue. Praesent eget tortor eu nulla porttitor aliquam. Sed auctor elementum quam vitae rhoncus.</p>
    </div>
    <span class="hint" style="top:529px">Swipe images to view.</span>
    <div class="photo photo--wall" role="img" aria-label="Photo of a white building"></div>
  </section>

  <!-- Event calendar -->
  <section class="screen screen--calendar">
    <div class="calendar-photo" role="img" aria-label="Photo of an old stone house behind trees"></div>
    <h1 class="cal-title cal-title--event">event</h1>
    <h1 class="cal-title cal-title--calendar">calendar</h1>
    <a class="nav-btn nav-btn--contents on-photo" style="left:298px;top:0"><small>return</small>contents<br>page</a>
    <a class="nav-btn nav-btn--cover" style="left:367px;top:0"><small>return</small>cover<br>page</a>
    <p class="cal-hint">Swipe striped bar to view other months. Click description to view full event.</p>

    <div class="month" style="left:10px;width:38px"><span class="month-name" style="left:-14px">Y</span><div class="month-stripes"></div>
      <span class="event-text" style="left:0;top:60px;width:40px">rem<br>scrip-<br>s en<br>Don't</span>
      <span class="event-text" style="left:0;top:162px;width:40px">nmodo<br>lacus<br>pre-<br>eleif-<br>is tor-<br>tim.</span>
      <span class="event-text" style="left:0;top:295px;width:40px">ia<br>llis<br>arius<br>e.</span>
    </div>
    <div class="month" style="left:56px;width:131px"><span class="month-name">FEBRUARY</span><div class="month-stripes"></div>
      <span class="event-date" style="left:0;top:122px">8th</span>
      <span class="event-text" style="left:38px;top:124px;width:90px">Another event! Definitely check this one out.</span>
      <span class="event-date" style="left:0;top:370px">29th</span>
      <span class="event-text" style="left:38px;top:372px;width:90px">Sed eleifend sagittis tortor in pretium.</span>
    </div>
    <div class="month" style="left:193px;width:130px"><span class="month-name">MARCH</span><div class="month-stripes"></div>
      <span class="event-date" style="left:0;top:69px">2nd</span>
      <span class="event-text" style="left:38px;top:71px;width:88px">Nunc magna erat, elementum sit amet dictum sit amet, imperdiet vel tortor. Fusce viverra sapien eu velit tempus vestibulum. Proin eleifend leo ac risus cursus lacinia.</span>
    </div>
    <div class="month" style="left:329px;width:94px"><span class="month-name">APRIL</span><div class="month-stripes"></div>
      <span class="event-date" style="left:0;top:126px">9th</span>
      <span class="event-text" style="left:38px;top:128px;width:90px">Sed eleifend sagittis fusce viverra sapien tortor in pretium.</span>
      <span class="event-date" style="left:0;top:236px">18th</span>
      <span class="event-text" style="left:38px;top:238px;width:90px">Aliquam erat turpis, lacinia metus sit amet vitae quis augue.</span>
    </div>
    <span class="swipe-tag">SWIPE</span>
  </section>

  <!-- Event calendar with add-event sheet -->
  <section class="screen screen--add-event">
    <div class="calendar-photo" role="img" aria-label="Photo of an old stone house behind trees"></div>
    <h1 class="cal-title cal-title--event">event</h1>
    <h1 class="cal-title cal-title--calendar">calendar</h1>
    <a class="nav-btn nav-btn--contents on-photo" style="left:298px;top:0"><small>return</small>contents<br>page</a>
    <a class="nav-btn nav-btn--cover" style="left:367px;top:0"><small>return</small>cover<br>page</a>
    <p class="cal-hint">Swipe striped bar to view other months. Click description to view full event.</p>
    <div class="month" style="left:10px;width:131px"><span class="month-name">JULY</span><div class="month-stripes"></div>
      <span class="event-date" style="left:0;top:236px">18th</span></div>
    <div class="month" style="left:283px;width:140px"><span class="month-name">SEPTEMBER</span><div class="month-stripes"></div></div>
    <span class="swipe-tag" style="left:393px">SWIPE</span>
    <div class="dim"></div>

    <div class="sheet">
      <div class="sheet-bar"><span class="sheet-btn">Cancel</span><span>Add Event</span><span class="sheet-btn sheet-btn--done">Done</span></div>
      <div class="field-group"><div class="field"><span class="val">An Event Relating to Things</span></div><div class="field"><span class="val">Somewhere</span></div></div>
      <div class="field-group"><div class="field"><b>Starts<br>Ends</b><span style="text-align:right">Sat, Dec 15 &nbsp;6:00 PM<br>9:00 PM &nbsp;›</span></div></div>
      <div class="field-group"><div class="field"><b>Repeat</b><span class="val">Never ›</span></div></div>
      <div class="field-group"><div class="field"><b>Alert</b><span class="val">None ›</span></div></div>
      <div class="field-group"><div class="field"><span class="ph">URL</span></div></div>
      <div class="field-group" style="height:90px"><div class="field"><span class="ph">Notes</span></div></div>
    </div>

    <div class="keyboard">
      <div class="key-row"><span class="key">Q</span><span class="key">W</span><span class="key">E</span><span class="key">R</span><span class="key">T</span><span class="key">Y</span><span class="key">U</span><span class="key">I</span><span class="key">O</span><span class="key">P</span><span class="key key--dark">⌫</span></div>
      <div class="key-row" style="padding-left:14px"><span class="key">A</span><span class="key">S</span><span class="key">D</span><span class="key">F</span><span class="key">G</span><span class="key">H</span><span class="key">J</span><span class="key">K</span><span class="key">L</span><span class="key key--dark" style="width:58px">return</span></div>
      <div class="key-row"><span class="key key--dark">⇧</span><span class="key">Z</span><span class="key">X</span><span class="key">C</span><span class="key">V</span><span class="key">B</span><span class="key">N</span><span class="key">M</span><span class="key">!<br>,</span><span class="key">?<br>.</span><span class="key key--dark">⇧</span></div>
      <div class="key-row"><span class="key key--dark" style="width:106px">.?123</span><span class="key" style="width:218px"></span><span class="key key--dark" style="width:56px">.?123</span><span class="key key--dark">⌨</span></div>
    </div>
  </section>

</main>
</body>
</html>
```